Out of town New Masters of Accounting

size of ad is 7” x 9.6”
please leave one inch on bottom for footer
We want to attract out of town students to join this master's in accounting program.
You DO NOT  have to use a picture of a person.
But if you do, it should be a  male with a white shirt and should not have long hair.(look like a young executive)
THE TEXT OF THE AD IS IN THE ATTACHMENTS
THE CAP LETTERS ARE THE INSTRUCTIONS

The age we are trying to attract is from 20-30 of ages.
- a clear ad .. the text should not take up the entire ad.. it should not be very crowded -
it should be an attractive ad that people would want to see and stand out
- the text very big and take up the entire ad

```html
<!DOCTYPE html>
<html lang="en">
<head>
<meta charset="utf-8">
<title>Remote Master in Accounting</title>
<link rel="stylesheet" href="https://fonts.googleapis.com/css2?family=Barlow+Semi+Condensed:wght@600;700&family=Barlow+Condensed:wght@500;600&family=Titillium+Web:wght@300;400;600;700&display=swap">
<style>
  :root{
    --orange:#e8760c;
    --yellow:#f3b41e;
    --gold-dark:#cf9b1a;
    --gold-line:#e2ac25;
    --red:#e20f1a;
    --ink:#1d1d1b;
    --grey:#5a5a5a;
    --white:#ffffff;
  }
  *{margin:0;padding:0;box-sizing:border-box}
  html,body{width:875px;height:1200px;overflow:hidden;background:var(--white)}
  .ad{position:relative;width:875px;height:1200px;overflow:hidden;background:var(--white);border:1px solid var(--ink);font-family:"Titillium Web",sans-serif}
  .shapes{position:absolute;left:0;top:0}
  .abs{position:absolute}

  .brand{left:84px;top:120px;display:flex;align-items:center;gap:10px;font-weight:600;font-size:22px;color:var(--orange)}
  .brand-dot{width:22px;height:22px;border-radius:50%;background:var(--orange)}

  .headline{left:430px;top:131px;font-family:"Barlow Semi Condensed",sans-serif;font-weight:700;color:var(--white);line-height:41px}
  .headline .l1,.headline .l2{font-size:49px;display:block}
  .headline .l3{font-size:41px;display:block}
  .divider{left:605px;top:139px;width:2px;height:64px;background:var(--yellow)}
  .audience{left:617px;top:136px;font-weight:600;font-size:22px;line-height:20.5px;color:var(--white)}

  .photo{left:0;top:277px;width:793px;height:470px;background:
    radial-gradient(ellipse 150px 170px at 300px 210px,#8a6a55 0%,rgba(138,106,85,0) 100%),
    radial-gradient(ellipse 220px 140px at 560px 190px,#cfa574 0%,rgba(207,165,116,0) 100%),
    linear-gradient(180deg,#1f1c22 0%,#3a3036 45%,#1a2540 100%)}

  .ribbon{left:0;top:636px;width:327px;height:63px}
  .ribbon-text{left:87px;top:638px;font-family:"Barlow Condensed",sans-serif;font-weight:600;font-size:26px;line-height:25px;color:var(--white)}

  .cap{left:330px;top:620px;width:300px;height:140px;background:radial-gradient(ellipse 50% 50% at 50% 50%,rgba(232,118,12,.95) 0%,rgba(232,118,12,.75) 55%,rgba(232,118,12,0) 100%)}

  .pitch{left:87px;top:771px;width:270px;font-weight:600;font-size:22px;line-height:26px;color:var(--orange);letter-spacing:.3px}
  .credential{left:87px;top:872px;width:300px;font-weight:400;font-size:19.5px;line-height:26.3px;color:var(--ink);letter-spacing:.2px}

  .advantage-title{left:482px;top:772px;font-weight:600;font-size:21px;line-height:28px;color:var(--grey)}
  .advantage-rule{left:482px;top:833px;width:250px;height:1px;background:var(--white)}
  .stat-icon{width:54px;height:54px;border-radius:50%;background:var(--white);left:485px}
  .stat-big{font-weight:300;color:var(--white);font-size:42px;line-height:40px}
  .stat-label{font-weight:400;color:var(--white);font-size:16.5px;line-height:20px}

  .footer-text{left:186px;top:1082px;width:590px;font-family:"Barlow Condensed",sans-serif;font-weight:500;font-size:14px;line-height:18.6px;color:var(--white)}
  .footer-text b{font-weight:600}
</style>
</head>
<body>
<main class="ad">
  <svg class="shapes" width="875" height="1200" viewBox="0 0 875 1200" aria-hidden="true">
    <path d="M365 277 V200 A143 143 0 0 1 508 57 H743 V277" fill="none" stroke="var(--yellow)" stroke-width="1"/>
    <path d="M379 277 V220 A150 150 0 0 1 529 70 H757 V277 Z" fill="var(--orange)"/>
    <polygon points="336,712 793,585 793,1200 446,1200 446,747 400,747" fill="var(--yellow)"/>
    <polygon points="793,585 863,617 793,646" fill="var(--gold-dark)"/>
    <polygon points="87,1063 875,1063 875,1162 168,1162" fill="var(--orange)"/>
  </svg>

  <div class="abs brand"><span class="brand-dot"></span>Merival Rankings</div>

  <h1 class="abs headline"><span class="l1">All new!</span><span class="l2">REMOTE</span><span class="l3">PROGRAM</span></h1>
  <div class="abs divider"></div>
  <p class="abs audience">for out<br>of town<br>students</p>

  <div class="abs photo" role="img" aria-label="Photo of a young executive in a navy suit and white shirt adjusting his tie, blurred city lights behind"></div>

  <svg class="abs ribbon" viewBox="0 0 327 63" aria-hidden="true"><polygon points="0,0 327,0 297,32 327,63 0,63" fill="var(--yellow)"/></svg>
  <p class="abs ribbon-text">Beginning August 17<br>New lower prices</p>

  <div class="abs cap" role="img" aria-label="Illustration of an orange graduation cap with tassel"></div>

  <svg class="shapes badge" width="875" height="1200" viewBox="0 0 875 1200" aria-hidden="true">
    <defs>
      <path id="seal-arc" d="M672 304 A60 60 0 0 1 792 304"/>
    </defs>
    <circle cx="732" cy="304" r="78" fill="var(--red)"/>
    <circle cx="732" cy="304" r="80" fill="none" stroke="var(--red)" stroke-width="14" stroke-linecap="round" stroke-dasharray="0 25.13"/>
    <circle cx="732" cy="304" r="52" fill="none" stroke="var(--white)" stroke-width="1"/>
    <circle cx="732" cy="304" r="49" fill="none" stroke="var(--white)" stroke-width=".6"/>
    <text font-family="Titillium Web, sans-serif" font-size="16" fill="var(--white)" letter-spacing=".5"><textPath href="#seal-arc" startOffset="50%" text-anchor="middle">A masters in only</textPath></text>
    <text x="732" y="336" text-anchor="middle" font-family="Barlow Semi Condensed, sans-serif" font-weight="700" font-size="82" fill="var(--white)">15</text>
    <polygon points="626,340 614,349 628,360 618,371 640,364" fill="var(--white)" stroke="var(--gold-line)" stroke-width="1"/>
    <polygon points="832,332 844,326 836,342 848,350 824,354" fill="var(--white)" stroke="var(--gold-line)" stroke-width="1"/>
    <path d="M626 338 Q730 350 834 330 L834 354 Q730 374 626 362 Z" fill="var(--white)" stroke="var(--gold-line)" stroke-width="1"/>
    <text x="731" y="361" text-anchor="middle" font-family="Titillium Web, sans-serif" font-weight="700" font-size="21" fill="var(--grey)">Months</text>
  </svg>

  <h2 class="abs pitch">Advance further in your career with a masters of science in accounting</h2>
  <p class="abs credential">Merival -- Halvorsen<br>Ridge University (HRU)<br>Master in Accounting Program<br>Received the highest possible<br>star rating</p>

  <h2 class="abs advantage-title">Keystone Career Alliance<br>Job Placement Advantage</h2>
  <div class="abs advantage-rule"></div>

  <div class="abs stat-icon" style="top:846px"><svg width="54" height="54" viewBox="0 0 54 54" aria-hidden="true"><rect x="18" y="15" width="18" height="23" rx="2" fill="none" stroke="var(--orange)" stroke-width="1.5"/><line x1="23" y1="21" x2="32" y2="21" stroke="var(--orange)" stroke-width="1.5"/><line x1="23" y1="26" x2="32" y2="26" stroke="var(--orange)" stroke-width="1.5"/><circle cx="20" cy="32" r="5" fill="var(--white)" stroke="var(--orange)" stroke-width="1.5"/></svg></div>
  <div class="abs stat-big" style="left:561px;top:852px">96%</div>
  <div class="abs stat-label" style="left:641px;top:852px">placement<br>rate</div>

  <div class="abs stat-icon" style="top:909px"><svg width="54" height="54" viewBox="0 0 54 54" aria-hidden="true"><rect x="15" y="17" width="10" height="8" fill="none" stroke="var(--orange)" stroke-width="1.5"/><rect x="29" y="17" width="10" height="8" fill="none" stroke="var(--orange)" stroke-width="1.5"/><rect x="15" y="29" width="10" height="8" fill="none" stroke="var(--orange)" stroke-width="1.5"/><rect x="29" y="29" width="10" height="8" fill="none" stroke="var(--orange)" stroke-width="1.5"/></svg></div>
  <div class="abs stat-big" style="left:564px;top:915px">8</div>
  <div class="abs stat-label" style="left:598px;top:917px">placement<br>coordinators</div>

  <div class="abs stat-icon" style="top:972px"><svg width="54" height="54" viewBox="0 0 54 54" aria-hidden="true"><circle cx="27" cy="20" r="5" fill="none" stroke="var(--orange)" stroke-width="1.5"/><circle cx="18" cy="34" r="4" fill="none" stroke="var(--orange)" stroke-width="1.5"/><circle cx="36" cy="34" r="4" fill="none" stroke="var(--orange)" stroke-width="1.5"/><path d="M22 40 A10 10 0 0 0 32 40" fill="none" stroke="var(--orange)" stroke-width="1.5"/></svg></div>
  <div class="abs stat-label" style="left:563px;top:982px;font-size:17px">Decades of relationships<br>with 100’s of firm</div>

  <p class="abs footer-text"><b>Footer text:</b> Lorem ipsum dolor sit amet, consectetur adipiscing elit. Aenean vel augue sed nibh venenatis fermentum a id nibh. Donec fermentum imperdiet leo, at blandit justo. Cras at est sit amet est dapibus ultricies ut non justo. Etiam sagittis, lorem id consectetur iaculis, est ipsum volutpat magna, et mollis felis ex ac tellus.</p>
</main>
</body>
</html>
```